Summit Builders Web Site / Business Cards

Construction Company that specializes in Water and Fire Damage, Residential ReModels, Landscaping and Building ADU (Accessory Dwelling Unit)

Growing and changing families often need additional space, and a remodeling project can often provide that. Adding a new area, or repurposing an existing one can satisfy this requirement.

Other times, homeowners want to update the look in their kitchen or bathroom with more than just a change of cabinetry or vanity doors and drawers. Whatever your needs are, Summit Builders has skilled workers who are bonded and insured, and ready to make your dreams and visions a reality.

Target Market(s)

Home Owners

Industry/Entity Type

Construction Company

Contact Information for Business Card

Center Logo with our information on the corners

Back side to be Logo Only
Contact Info
CSLB License # 4829516
info@summitbuildersca.example
www.summitbuildersca.example

Coding

Coded - Design and coding required

Number of Pages Required

5+ page

Font styles to use
Serif
Sans Serif

Requirements
Must have
• Using our Logo Colors
Home
About Us
Services
Projects / Portfolio
Contact Us
Nice to have
• Colors matching our Logo
Should not have
• Black because it doesnt match our logo

```html
<!DOCTYPE html>
<html lang="en">
<head>
<meta charset="utf-8">
<title>Summit Builders — Home Construction &amp; Remodeling</title>
<link href="https://fonts.googleapis.com/css2?family=Jost:wght@400;500;600;700&family=Raleway:wght@400;500&display=swap" rel="stylesheet">
<style>
:root{
  --orange:#ee7524;
  --orange-deep:#e0651a;
  --peach:#fdeadc;
  --ink:#2a2a2e;
  --text:#4a4a4f;
  --mist:#f3f4f7;
  --card:#eceef3;
  --white:#ffffff;
  --footer:#2e2f33;
}
*{box-sizing:border-box;margin:0;padding:0}
html,body{width:1200px;height:3856px;overflow:hidden;background:var(--white)}
body{font-family:"Jost",sans-serif;color:var(--ink)}
.page{position:relative;width:1200px;height:3856px;overflow:hidden}
.abs{position:absolute}
.center{text-align:center;left:0;width:1200px}

/* hero */
.hero{left:0;top:0;width:1200px;height:609px;background:linear-gradient(160deg,#d9d6d1 0%,#bdb6ab 35%,#8c8378 60%,#3d4356 100%)}
.hero-shade{left:0;top:0;width:1200px;height:609px;background:linear-gradient(180deg,rgba(0,0,0,.05),rgba(0,0,0,.28))}
.topbar{left:0;top:22px;width:1200px;height:90px;background:var(--orange)}
.brand{left:162px;top:52px;color:var(--white);font-weight:600;font-size:22px;letter-spacing:1px;display:flex;align-items:center;gap:10px}
.brand-mark{width:16px;height:16px;background:var(--white)}
.nav{left:461px;top:58px;display:flex;gap:23px;font-size:14px;color:var(--white);letter-spacing:.5px}
.nav .active{font-weight:600}
.btn{display:flex;align-items:center;justify-content:center;font-weight:500;letter-spacing:1px;font-size:15px}
.btn-quote-top{left:904px;top:49px;width:134px;height:37px;background:var(--white);color:var(--orange)}
.hero-title{top:332px;font-weight:700;font-size:46px;line-height:60px;color:var(--white);letter-spacing:1px;text-shadow:0 2px 6px rgba(0,0,0,.4)}
.hero-sub{top:456px;font-weight:600;font-size:23px;color:var(--white);letter-spacing:1.5px;text-shadow:0 2px 5px rgba(0,0,0,.4)}
.btn-hero{left:525px;top:504px;width:150px;height:38px;background:var(--orange);color:var(--white)}

/* section heads */
.sec-icon{width:12px;height:12px;left:594px;background:var(--orange)}
.sec-icon.light{background:var(--white)}
.sec-title{font-weight:700;font-size:36px;letter-spacing:1px}
.sec-title span{font-weight:400}
.sec-sub{font-size:17px;color:var(--orange);letter-spacing:1px}

/* about */
.about-frame{left:270px;top:840px;width:213px;height:240px;border:14px solid #fde3d1}
.photo-a{left:162px;top:821px;width:272px;height:222px;background:linear-gradient(135deg,#f1f0ee,#c7c2bb)}
.photo-b{left:322px;top:875px;width:251px;height:222px;background:linear-gradient(135deg,#6f90b8,#c9a27a 60%,#8a6a4c);border:4px solid var(--white)}
.about-text{left:628px;top:838px;width:410px;font-family:"Raleway",sans-serif;font-size:13px;line-height:27px;color:var(--text);text-align:justify}
.about-text p+p{margin-top:8px}

.feature{top:1159px;width:205px;height:205px;background:linear-gradient(160deg,#f9fafc,var(--card));text-align:center}
.feature svg{position:absolute;left:60px;top:30px}
.feature h3{position:absolute;top:132px;left:0;width:205px;font-weight:500;font-size:18px;line-height:23px}

/* services */
.services{left:0;top:1441px;width:1200px;height:612px;background:linear-gradient(180deg,#f08a3e,#ee7524 50%,#e9722a)}
.services-title{top:1540px;color:var(--white)}
.svc{top:1613px;width:206px;height:285px;background:var(--white);box-shadow:0 6px 16px rgba(0,0,0,.15)}
.svc-img{left:0;top:0;width:206px;height:179px}
.svc-badge{left:79px;top:156px;width:48px;height:48px;border-radius:50%;background:var(--orange);border:3px solid var(--white)}
.svc h3{position:absolute;top:214px;left:0;width:206px;text-align:center;font-weight:500;font-size:18px;line-height:22px}
.btn-contact{left:503px;top:1937px;width:194px;height:39px;background:var(--white);color:var(--orange)}

/* stats */
.stats{left:0;top:2053px;width:1200px;height:276px;background:var(--peach)}
.stat{top:2144px}
.stat .num{position:absolute;top:64px;left:0;white-space:nowrap;font-weight:600;font-size:30px}
.stat .num small{font-size:14px;font-weight:600;margin-left:6px}

/* projects */
.proj-feature{left:162px;top:2506px;width:285px;height:326px;background:linear-gradient(135deg,#d08a55,#a2643d)}
.proj-overlay{left:172px;top:2516px;width:265px;height:306px;background:rgba(238,117,36,.88);color:var(--white);text-align:center}
.proj-overlay h3{margin-top:120px;font-weight:500;font-size:18px;letter-spacing:.5px}
.proj-overlay p{margin:6px 16px 0;font-family:"Raleway",sans-serif;font-size:11.5px;line-height:19px}
.next{left:728px;top:2647px;width:44px;height:44px;border-radius:50%;background:var(--white);box-shadow:0 2px 8px rgba(0,0,0,.25)}
.btn-view{left:540px;top:2871px;width:120px;height:39px;background:var(--orange);color:var(--white)}

/* reviews */
.reviews{left:0;top:2988px;width:1200px;height:543px;background:var(--mist)}
.review{top:3160px;width:405px;height:293px;background:var(--white);box-shadow:0 4px 14px rgba(0,0,0,.05)}
.review p{position:absolute;left:32px;top:88px;width:340px;font-family:"Raleway",sans-serif;font-size:12.5px;line-height:24.5px;color:var(--text)}
.quote-mark{position:absolute;left:16px;top:54px;font-size:110px;line-height:1;color:#f5f3f3;font-family:"Jost",sans-serif}
.avatar{position:absolute;left:32px;top:212px;width:52px;height:52px;border-radius:50%;background:linear-gradient(135deg,#d8c3b3,#8e7766);border:2px solid var(--orange)}
.who{position:absolute;left:96px;top:216px}
.who b{display:block;color:var(--orange);font-weight:500;font-size:17px}
.who span{font-family:"Raleway",sans-serif;font-size:12.5px;color:var(--text)}
.arrow-btn{top:3313px;width:28px;height:28px;border-radius:50%}

/* footer */
.footer{left:0;top:3531px;width:1200px;height:325px;background:linear-gradient(160deg,#3a3b3f,var(--footer) 55%,#45464b)}
.fnav{top:3608px;font-size:14px;color:var(--white);letter-spacing:.5px}
.fcontact{top:3706px;display:flex;align-items:flex-start;gap:14px;color:var(--white);font-size:13px;line-height:20px}
.fcontact .dot{width:36px;height:36px;border-radius:50%;background:var(--orange);flex:none;display:flex;align-items:center;justify-content:center}
.fcontact b{font-weight:600;display:block}
.copy{left:162px;top:3803px;font-size:12.5px;color:#d9d9dc}
.copy strong{color:var(--white);font-weight:500;font-size:14px}
.iso{left:816px;top:3805px;font-size:12.5px;color:#d9d9dc}
.social{top:3800px;width:24px;height:24px;border-radius:50%}
</style>
</head>
<body>
<div class="page">

  <!-- hero -->
  <div class="abs hero" role="img" aria-label="Bright white kitchen with marble counters, brass faucet and gold pendant lights"></div>
  <div class="abs hero-shade"></div>
  <header class="abs topbar"></header>
  <div class="abs brand"><span class="brand-mark"></span>Summit Builders</div>
  <nav class="abs nav">
    <span class="active">HOME</span><span>ABOUT US</span><span>SERVICES</span><span>PROJECTS</span><span>CONTACT US</span>
  </nav>
  <div class="abs btn btn-quote-top">GET A QUOTE</div>
  <h1 class="abs center hero-title">HOME CONSTRUCTION<br>&amp; REMODELING</h1>
  <div class="abs center hero-sub">THE BEST CHOOSE US BECAUSE WE DELIVER</div>
  <div class="abs btn btn-hero">GET A QUOTE</div>

  <!-- about -->
  <span class="abs sec-icon" style="top:688px"></span>
  <h2 class="abs center sec-title" style="top:707px">ABOUT SUMMIT <span>BUILDERS</span></h2>
  <div class="abs center sec-sub" style="top:761px">WE DELIVER LANDMARK PROJECTS</div>
  <div class="abs about-frame"></div>
  <div class="abs photo-a" role="img" aria-label="White kitchen interior with skylight"></div>
  <div class="abs photo-b" role="img" aria-label="Two workers in hard hats cutting wood with a circular saw"></div>
  <div class="abs about-text">
    <p>We are rethoric question ran over her cheek When she reached the first hills of the Italic Mountains, she had a last view back on the skyline of her hometown Bookmarksgrove, the headline of Alphabet Village &amp; the subline of her own road, the Line Lane.</p>
    <p>Lorem ipsum dolor sit amet, consectetuer adipiscing elit, sed dia nonummy nibh euismod tincidunt ut laoreet dolore magna aliqu m erat volutpat. Ut wisi enim ad minim veniam, quis nostrud exer citation ullamcorper suscipit lobortis nisl ut aliquip.</p>
  </div>

  <div class="abs feature" style="left:162px">
    <svg width="86" height="86" viewBox="0 0 86 86"><rect x="18" y="18" width="50" height="50" rx="8" transform="rotate(45 43 43)" fill="var(--orange)"/><circle cx="43" cy="40" r="11" fill="none" stroke="#fff" stroke-width="2"/><path d="M37 50 35 60 43 56 51 60 49 50" fill="none" stroke="#fff" stroke-width="2"/></svg>
    <h3>We've Repution<br>For Excellence</h3>
  </div>
  <div class="abs feature" style="left:385px">
    <svg width="86" height="86" viewBox="0 0 86 86"><rect x="18" y="18" width="50" height="50" rx="8" transform="rotate(45 43 43)" fill="var(--orange)"/><path d="M28 42 36 34 43 40 50 34 58 42 47 53 39 53Z" fill="none" stroke="#fff" stroke-width="2" stroke-linejoin="round"/></svg>
    <h3>We Build<br>Partnerships</h3>
  </div>
  <div class="abs feature" style="left:609px">
    <svg width="86" height="86" viewBox="0 0 86 86"><rect x="18" y="18" width="50" height="50" rx="8" transform="rotate(45 43 43)" fill="var(--orange)"/><path d="M31 41H37V56H31ZM37 42 44 30C47 30 47 34 46 38H55L52 55H37" fill="none" stroke="#fff" stroke-width="2" stroke-linejoin="round"/></svg>
    <h3>Guided By<br>Commitment</h3>
  </div>
  <div class="abs feature" style="left:833px">
    <svg width="86" height="86" viewBox="0 0 86 86"><rect x="18" y="18" width="50" height="50" rx="8" transform="rotate(45 43 43)" fill="var(--orange)"/><g fill="none" stroke="#fff" stroke-width="2"><circle cx="34" cy="38" r="4"/><circle cx="43" cy="36" r="4"/><circle cx="52" cy="38" r="4"/><path d="M28 52V47H40V52M37 50V44H49V50M46 52V47H58V52"/></g></svg>
    <h3>A Team Of<br>Professionals</h3>
  </div>

  <!-- services -->
  <section class="abs services" role="img" aria-label="Orange-tinted photo of a suburban house behind the services"></section>
  <span class="abs sec-icon light" style="top:1522px"></span>
  <h2 class="abs center sec-title services-title">OUR SERVICES</h2>

  <div class="abs svc" style="left:162px">
    <div class="abs svc-img" style="background:linear-gradient(135deg,#8d7866,#4e4038)" role="img" aria-label="Fire damaged room interior"></div>
    <div class="abs svc-badge"></div>
    <h3>Water And<br>Fire Damage</h3>
  </div>
  <div class="abs svc" style="left:385px">
    <div class="abs svc-img" style="background:linear-gradient(180deg,#b9c6d4,#a89a8b)" role="img" aria-label="House under residential remodel"></div>
    <div class="abs svc-badge"></div>
    <h3>Residential<br>ReModels</h3>
  </div>
  <div class="abs svc" style="left:609px">
    <div class="abs svc-img" style="background:linear-gradient(180deg,#7e9a6e,#4f8a3a)" role="img" aria-label="Landscaped front garden with lawn and flowers"></div>
    <div class="abs svc-badge"></div>
    <h3 style="top:224px">Landscaping</h3>
  </div>
  <div class="abs svc" style="left:833px">
    <div class="abs svc-img" style="background:linear-gradient(180deg,#c7d3dc,#9bb08c)" role="img" aria-label="Small white accessory dwelling unit with porch"></div>
    <div class="abs svc-badge"></div>
    <h3 style="top:224px">Building ADU</h3>
  </div>
  <div class="abs btn btn-contact">CONTACT US TODAY</div>

  <!-- stats -->
  <section class="abs stats"></section>
  <div class="abs stat" style="left:162px">
    <svg width="54" height="52" viewBox="0 0 54 52" fill="none" stroke="var(--orange)" stroke-width="2"><rect x="2" y="2" width="40" height="48"/><path d="M10 42 20 12 30 42M44 8 52 16 40 46 34 46 34 40Z"/></svg>
    <div class="num">53<small>Total Projects</small></div>
  </div>
  <div class="abs stat" style="left:386px">
    <svg width="60" height="52" viewBox="0 0 60 52" fill="none" stroke="var(--orange)" stroke-width="2"><circle cx="12" cy="18" r="6"/><circle cx="30" cy="14" r="6"/><circle cx="48" cy="18" r="6"/><path d="M2 48V32H22V48M20 44V26H40V44M38 48V32H58V48"/></svg>
    <div class="num">371<small>Staff Members</small></div>
  </div>
  <div class="abs stat" style="left:610px">
    <svg width="58" height="52" viewBox="0 0 58 52" fill="none" stroke="var(--orange)" stroke-width="2"><rect x="2" y="10" width="54" height="30" rx="4"/><path d="M8 18H50M8 25H50M8 32H40"/></svg>
    <div class="num">15<small>Working In States</small></div>
  </div>
  <div class="abs stat" style="left:834px">
    <svg width="56" height="54" viewBox="0 0 56 54" fill="none" stroke="var(--orange)" stroke-width="2"><circle cx="28" cy="30" r="20"/><path d="M28 30V18M28 30 38 36M22 4H34M28 4V10"/></svg>
    <div class="num">2,600<small>Hours For Work</small></div>
  </div>

  <!-- projects -->
  <span class="abs sec-icon" style="top:2409px"></span>
  <h2 class="abs center sec-title" style="top:2427px">OUR PROJECTS</h2>
  <div class="abs proj-feature" role="img" aria-label="House exterior used for remodeling works"></div>
  <div class="abs proj-overlay">
    <h3>REMODELING WORKS</h3>
    <p>Lorem ipsum dolor sit amet, consect etuer adipiscing elit, sed diam nonummy nibh euismod tincidunt ut laoreet.</p>
  </div>
  <div class="abs" style="left:452px;top:2506px;width:145px;height:158px;background:linear-gradient(135deg,#d8d2c9,#8c7e70)" role="img" aria-label="Remodeled bathroom with tub"></div>
  <div class="abs" style="left:452px;top:2670px;width:145px;height:162px;background:linear-gradient(180deg,#bcd0e3,#6a7f92)" role="img" aria-label="School building exterior"></div>
  <div class="abs" style="left:601px;top:2506px;width:146px;height:158px;background:linear-gradient(180deg,#6f7fa8,#3c4a6a)" role="img" aria-label="Two-story house at dusk"></div>
  <div class="abs" style="left:601px;top:2670px;width:146px;height:162px;background:linear-gradient(180deg,#a9b4a3,#4f8a3a)" role="img" aria-label="House with green front lawn"></div>
  <div class="abs" style="left:751px;top:2506px;width:287px;height:326px;background:linear-gradient(135deg,#d7d0c6,#5e4a3c)" role="img" aria-label="Kitchen with dark cabinets and marble island"></div>
  <div class="abs next"><svg width="44" height="44" viewBox="0 0 44 44"><path d="M19 15 26 22 19 29" fill="none" stroke="var(--ink)" stroke-width="2"/></svg></div>
  <div class="abs btn btn-view">VIEW ALL</div>

  <!-- reviews -->
  <section class="abs reviews"></section>
  <span class="abs sec-icon" style="top:3067px"></span>
  <h2 class="abs center sec-title" style="top:3086px">CLIENT REVIEWS</h2>
  <div class="abs review" style="left:177px">
    <span class="quote-mark">&ldquo;</span>
    <p>And for all the wonderful work you and your crew are doing. Our team has nothing but good things to say - we are really fortunate to have found you for this project!</p>
    <div class="avatar" role="img" aria-label="Client portrait"></div>
    <div class="who"><b>Marcus Brennan</b><span>Chairman NRB</span></div>
  </div>
  <div class="abs review" style="left:618px">
    <span class="quote-mark">&ldquo;</span>
    <p>Summit Builders is one of the best general contractors we've worked with. The entire team tactfully delivered a project of exceptional quality while staying on schedule and under budget.</p>
    <div class="avatar" role="img" aria-label="Client portrait"></div>
    <div class="who"><b>Helen Marsh</b><span>Project Manager</span></div>
  </div>
  <svg class="abs arrow-btn" style="left:91px" viewBox="0 0 28 28"><circle cx="14" cy="14" r="13" fill="none" stroke="#c9c9cd" stroke-width="1.5"/><path d="M19 14H9M13 10 9 14 13 18" fill="none" stroke="#c9c9cd" stroke-width="1.5"/></svg>
  <svg class="abs arrow-btn" style="left:1080px" viewBox="0 0 28 28"><circle cx="14" cy="14" r="13" fill="none" stroke="var(--ink)" stroke-width="1.5"/><path d="M9 14H19M15 10 19 14 15 18" fill="none" stroke="var(--ink)" stroke-width="1.5"/></svg>

  <!-- footer -->
  <footer class="abs footer" role="img" aria-label="Darkened kitchen interior behind the footer"></footer>
  <div class="abs fnav" style="left:277px">HOME</div>
  <div class="abs fnav" style="left:397px">ABOUT US</div>
  <div class="abs fnav" style="left:546px">SERVICES</div>
  <div class="abs fnav" style="left:688px">PROJECTS</div>
  <div class="abs fnav" style="left:832px">CONTACT US</div>

  <div class="abs fcontact" style="left:195px">
    <span class="dot"><svg width="16" height="18" viewBox="0 0 16 18"><path d="M8 17C3 11 2 9 2 7A6 6 0 0 1 14 7C14 9 13 11 8 17Z" fill="#fff"/><circle cx="8" cy="7" r="2.2" fill="var(--orange)"/></svg></span>
    <div>418 W Harbor Crest Ave,<br>Tustin, CA 92780</div>
  </div>
  <div class="abs fcontact" style="left:551px">
    <span class="dot"><svg width="16" height="16" viewBox="0 0 16 16"><path d="M3 1 6 1 7 5 5 6C6 8 8 10 10 11L11 9 15 10V13C15 14 14 15 13 15 7 15 1 9 1 3 1 2 2 1 3 1Z" fill="#fff"/></svg></span>
    <div><b>PHONE</b>555-013-2740</div>
  </div>
  <div class="abs fcontact" style="left:767px">
    <span class="dot"><svg width="16" height="16" viewBox="0 0 16 16"><path d="M1 7 15 1 11 15 8 9Z" fill="#fff"/></svg></span>
    <div><b>EMAIL</b>hello@summitbuildersca.example</div>
  </div>

  <div class="abs copy">Copyright &copy; 2020 <strong>SUMMIT BUILDERS.</strong> All Rights Reserved.</div>
  <div class="abs iso">ISO 9001:2017</div>
  <span class="abs social" style="left:919px;background:#3b5ea8"></span>
  <span class="abs social" style="left:950px;background:#1c7bb5"></span>
  <span class="abs social" style="left:981px;background:#2ba3e0"></span>
  <span class="abs social" style="left:1012px;background:#d9302c"></span>

</div>
</body>
</html>
```